Simple and clean

We need a business card design for a new company called Dwelling Owl. It is a search engine to find current properties for sale or rent in New Zealand market.
We have already a colour scheme that we would like people to use.
Light brown: #D4CCB0
Light green: #D6E4D4
Green: #669966
Black/White
It is OK to divert from this colour scheme slightly as long as there is a green component to the business card.
Final design should be clean, simple and should communicate the nature of the business.
Target Market(s)
- First home buyers
- Real estate agents
- People seeking rentals
Industry/Entity Type
Business
Requirements
Must have
- Use those or similar colours.
Light brown: #D4CCB0
Light green: #D6E4D4
Green: #669966
Black/White

```html
<!DOCTYPE html>
<html lang="en">
<head>
<meta charset="utf-8">
<title>Dwelling Owl — Business Card</title>
<link rel="stylesheet" href="https://fonts.googleapis.com/css2?family=Source+Sans+3:wght@400;600;700&display=swap">
<style>
  :root {
    --backdrop: #d5e0d4;
    --card-white: #ffffff;
    --brand-green: #3b7139;
    --icon-green: #3e6f3a;
    --text-dark: #1a1a1a;
    --text-green: #3a6a36;
    --vignette: rgba(60, 60, 60, 0.38);
  }
  * { margin: 0; padding: 0; box-sizing: border-box; }
  html, body {
    width: 1200px;
    height: 900px;
    overflow: hidden;
    background: var(--backdrop);
    font-family: "Source Sans 3", "Myriad Pro", Arial, sans-serif;
  }
  .business-card {
    position: absolute;
    left: 232px;
    top: 240px;
    width: 736px;
    height: 420px;
    background: var(--card-white);
    box-shadow: inset 0 0 34px var(--vignette);
  }
  .brand {
    position: absolute;
    top: 40px;
    left: 0;
    width: 100%;
    display: flex;
    align-items: center;
    justify-content: center;
    gap: 18px;
  }
  .brand-mark {
    width: 44px;
    height: 44px;
    border-radius: 50%;
    background: var(--brand-green);
  }
  .brand-name {
    font-size: 56px;
    font-weight: 700;
    color: var(--text-dark);
    letter-spacing: -0.5px;
  }
  .name-band {
    position: absolute;
    left: 0;
    top: 152px;
    width: 100%;
    height: 92px;
    background: var(--brand-green);
    color: var(--card-white);
    text-align: center;
  }
  .person-name {
    margin-top: 10px;
    font-size: 31px;
    font-weight: 700;
    line-height: 38px;
  }
  .person-role {
    font-size: 24px;
    font-weight: 400;
    line-height: 30px;
  }
  .contact-list {
    position: absolute;
    right: 32px;
    top: 300px;
    list-style: none;
  }
  .contact-item {
    display: flex;
    align-items: center;
    justify-content: flex-end;
    gap: 8px;
    height: 32px;
    font-size: 22px;
    color: var(--text-green);
  }
  .contact-badge {
    width: 24px;
    height: 24px;
    background: var(--icon-green);
    color: var(--card-white);
    font-size: 15px;
    font-weight: 700;
    display: flex;
    align-items: center;
    justify-content: center;
  }
</style>
</head>
<body>
  <div class="business-card">
    <div class="brand">
      <span class="brand-mark"></span>
      <span class="brand-name">Dwelling Owl</span>
    </div>
    <div class="name-band">
      <p class="person-name">Mark Tane</p>
      <p class="person-role">Director</p>
    </div>
    <ul class="contact-list">
      <li class="contact-item"><span>+000-000-0000</span><span class="contact-badge">T</span></li>
      <li class="contact-item"><span>mark@dwellingowl.co.nz</span><span class="contact-badge">E</span></li>
      <li class="contact-item"><span>www.dwellingowl.co.nz</span><span class="contact-badge">W</span></li>
    </ul>
  </div>
</body>
</html>
```